M Website

We need a website design for a construction plant company. You may use a combination of our photos and the stock images. See the logo for company colours. It also be of great value to see moving pictures like the ones on the link: https://www.quindellworks.co.za/copy-of-about-us. See our uploaded files for content.

Target Market(s)

Construction

Number of Pages Required

5+ page

```html
<!DOCTYPE html>
<html lang="en">
<head>
<meta charset="utf-8">
<title>Tarvo Logistic Plant</title>
<link href="https://fonts.googleapis.com/css2?family=Open+Sans:wght@300;400;600;700&display=swap" rel="stylesheet">
<style>
:root{
  --orange:#f39322;
  --orange-deep:#ee7d1a;
  --orange-light:#f9ab3f;
  --yellow:#f7c01c;
  --red:#e9502a;
  --ink:#2b2b2b;
  --text:#555;
  --muted:#8a8a8a;
  --line:#e2e2e2;
  --dark:#2f2f2f;
  --white:#fff;
}
*{box-sizing:border-box;margin:0;padding:0}
html,body{width:1200px;height:4467px;overflow:hidden}
body{font-family:"Open Sans",Arial,sans-serif;color:var(--text);background:var(--white);position:relative}
.wrap{width:1044px;margin:0 auto;position:relative}
a{color:inherit;text-decoration:none}

/* top bar */
.topbar{height:50px;background:var(--orange);color:var(--white);font-size:15px}
.topbar .wrap{display:flex;align-items:center;height:50px}
.social{display:flex}
.social span{width:46px;height:50px;display:flex;align-items:center;justify-content:center;border-right:1px solid rgba(255,255,255,.35)}
.social span i{width:12px;height:12px;background:var(--white);border-radius:2px;display:block}
.contact-top{margin-left:auto;display:flex;align-items:center;height:50px}
.contact-top div{display:flex;align-items:center;gap:10px;padding:0 22px;height:50px;border-left:1px solid rgba(255,255,255,.35)}

/* nav */
.nav{height:130px}
.nav .wrap{display:flex;align-items:center;height:130px}
.brand{display:flex;align-items:center;gap:12px;font-size:34px;font-weight:700;color:var(--ink)}
.brand-dot{width:34px;height:34px;border-radius:50%;background:var(--orange)}
.menu{display:flex;gap:44px;margin-left:70px;font-size:17px;color:#777}
.menu .active{color:var(--red);font-weight:600;position:relative}
.menu .active:after{content:"";position:absolute;left:50%;top:38px;margin-left:-10px;border:10px solid transparent;border-bottom:14px solid var(--red);border-top:0}
.search{margin-left:auto;width:250px;height:42px;border:1px solid var(--line);border-radius:21px;display:flex;align-items:center;padding:0 16px;font-size:14px;color:#999;justify-content:space-between}

/* hero */
.hero{height:570px;position:relative;overflow:hidden;
  background:linear-gradient(90deg,rgba(0,0,0,0) 55%,rgba(200,140,60,.45) 80%,rgba(120,90,60,.35) 100%),
             linear-gradient(180deg,#dfe6ea 0%,#c9d3d8 45%,#aeb8bc 70%,#8b9599 100%)}
.hero h1{position:absolute;left:83px;top:155px;font-size:72px;line-height:86px;font-weight:400;color:var(--white)}
.hero h1 .first{color:var(--red);font-weight:700;display:block}
.hero h1 .hl{color:var(--yellow);font-weight:600}
.hero h1 .hl2{color:var(--orange);font-weight:600}
.dots{position:absolute;left:560px;bottom:20px;display:flex;gap:10px}
.dots i{width:16px;height:16px;border-radius:50%;background:#fff;border:2px solid #ddd;display:block}
.dots i.on{background:var(--orange);border-color:var(--orange)}

/* welcome */
.welcome{height:465px;padding-top:70px}
.welcome .wrap{display:flex;justify-content:space-between}
.welcome-text{width:540px}
.welcome h2{font-size:36px;font-weight:400;color:var(--ink);margin-bottom:28px;white-space:nowrap}
.welcome p{font-size:14px;line-height:24px;color:var(--muted);margin-bottom:20px}
.btn{display:inline-block;background:var(--orange);color:var(--white);font-size:16px;font-weight:600;padding:14px 26px;border-radius:26px;text-transform:uppercase}
.welcome-photo{width:470px;height:332px;background:linear-gradient(160deg,#c7d6dc 0%,#9aa48b 40%,#3a3b35 70%,#7c7f72 100%)}

/* mission */
.band{height:340px;display:flex;color:var(--white)}
.band>div{width:50%;padding:60px 0 0}
.band .left{background:var(--orange-light);padding-left:78px;padding-right:60px}
.band .right{background:var(--orange-deep);padding-left:46px;padding-right:78px}
.band h3{font-size:36px;font-weight:400;line-height:44px;margin-bottom:18px}
.band .right h3{max-width:400px}
.band p{font-size:14px;line-height:24px}
.band ul{list-style:none;font-size:14px;line-height:20px}
.band li{display:flex;gap:12px;margin-bottom:10px}
.band li:before{content:"";width:13px;height:13px;border-radius:50%;background:var(--white);flex:none;margin-top:4px}

/* services */
.services{height:685px;padding-top:78px;text-align:center}
.section-title{font-size:38px;font-weight:400;color:var(--ink)}
.section-sub{font-size:14px;color:var(--muted);line-height:22px;margin-top:28px}
.cards{display:flex;justify-content:space-between;margin-top:50px;text-align:center}
.card{width:333px;height:393px;border:1px solid var(--line);box-shadow:0 2px 6px rgba(0,0,0,.06)}
.card-photo{height:215px;background:linear-gradient(180deg,#9fc4e0 0%,#b9b69a 50%,#4f4f47 100%);clip-path:polygon(0 0,100% 0,100% 88%,50% 100%,0 88%)}
.card h4{font-size:22px;font-weight:400;color:var(--ink);margin-top:16px}
.card p{font-size:14px;line-height:22px;color:var(--muted);margin-top:10px}
.card .more{display:block;color:var(--orange);font-size:14px;font-weight:600;margin-top:12px;text-decoration:underline}

/* achieving */
.achieve{height:545px;background:linear-gradient(180deg,#3a3a3a,#262626);position:relative;color:var(--white)}
.city{position:absolute;left:60px;top:20px;width:480px;height:500px;background:linear-gradient(180deg,#4a5866 0%,#7d93a6 45%,#5d7a4b 85%,#3a3a3a 100%);opacity:.85}
.achieve-body{position:absolute;left:584px;top:60px;width:538px}
.achieve h3{font-size:38px;font-weight:400;color:var(--yellow)}
.achieve .lead{font-size:14px;margin-top:22px}
.icons{margin-top:30px;height:117px;background:#7c7c7c;display:flex;align-items:center;justify-content:space-around;padding:0 20px}
.icons span{width:68px;height:68px;border:2px solid var(--white);display:flex;align-items:center;justify-content:center}
.icons span.on{background:var(--yellow);border-color:var(--yellow)}
.achieve h4{font-size:24px;font-weight:400;color:var(--yellow);margin-top:54px}
.achieve .desc{font-size:14px;line-height:22px;margin-top:14px}

/* projects */
.projects{height:675px;padding-top:50px;text-align:center}
.filters{margin-top:34px;font-size:14px;color:var(--muted)}
.filters span{margin:0 10px}
.filters .on{color:var(--orange);font-weight:600}
.grid{display:grid;grid-template-columns:repeat(4,244px);gap:30px 22px;margin-top:40px}
.tile{height:208px;position:relative}
.t1{background:linear-gradient(180deg,#b5c6d2,#c89a35 60%,#4d4335)}
.t2{background:linear-gradient(180deg,#7f9fc4,#b9723c 50%,#7b5532)}
.t3{background:linear-gradient(180deg,#a6a79a,#d98a2f 55%,#78746a)}
.t4{background:linear-gradient(180deg,#524c49,#8c6b4f 50%,#3b3532)}
.t5{background:linear-gradient(180deg,#c8d4da,#e0582d 55%,#5f5a56)}
.t6{background:linear-gradient(180deg,#6f6154,#d07d2e 55%,#3a3430)}
.t7{background:linear-gradient(180deg,#888a86,#d9a046 50%,#4e4a45)}
.t8{background:linear-gradient(180deg,#b4bcb8,#d8a12d 55%,#5a5652)}
.tile.feature{border:6px solid var(--orange)}
.tile .label{position:absolute;left:0;right:0;bottom:18px;background:rgba(200,110,20,.75);color:#fff;padding:8px 0}
.tile .label b{display:block;font-size:17px;font-weight:600}
.tile .label small{font-size:12px}

/* contact form */
.ready{height:567px;background:linear-gradient(180deg,#f6a741,#ef8a22);padding-top:64px;text-align:center;color:var(--white)}
.ready h2{font-size:38px;font-weight:400}
.ready p{font-size:14px;margin-top:18px}
.form{width:676px;margin:34px auto 0;display:grid;grid-template-columns:1fr 1fr;gap:15px 10px;text-align:left}
.field{height:57px;background:var(--white);border-radius:3px;color:#777;font-size:14px;padding:18px 14px}
.field.full{grid-column:1/3;height:99px}
.submit{grid-column:1/3;justify-self:center;width:167px;height:57px;background:#111;color:#fff;font-size:15px;font-weight:600;display:flex;align-items:center;justify-content:center;border-radius:3px;text-transform:uppercase}

/* footer */
.footer{height:360px;padding-top:55px}
.footer .wrap{display:grid;grid-template-columns:270px 268px 268px 238px}
.footer .brand{font-size:28px}
.footer .brand-dot{width:28px;height:28px}
.footer .about{font-size:13px;line-height:21px;color:var(--muted);margin-top:20px;width:230px}
.footer .about u{color:var(--ink)}
.footer h5{font-size:19px;font-weight:400;color:var(--ink);margin-bottom:18px}
.links{list-style:none;font-size:13px;color:var(--muted)}
.links li{display:flex;align-items:center;gap:10px;margin-bottom:9px}
.links li:before{content:"";width:8px;height:8px;border-radius:50%;border:2px solid var(--orange)}
.links li.on{color:var(--red)}
.touch{display:flex;gap:14px;font-size:13px;color:var(--muted);line-height:20px;margin-bottom:20px}
.touch b{color:var(--orange);font-weight:600}
.news p{font-size:13px;line-height:21px;color:var(--muted)}
.sub{display:flex;margin-top:20px;height:50px;border:1px solid var(--line);align-items:center;font-size:13px;color:#777}
.sub span{flex:1;padding-left:12px;display:flex;gap:8px;align-items:center}
.sub i{width:50px;height:50px;background:var(--red);display:flex;align-items:center;justify-content:center}
.copy{position:absolute;left:0;right:0;top:4387px;height:80px;background:var(--orange);color:var(--white);font-size:13px;display:flex;align-items:center;justify-content:center}
</style>
</head>
<body>

<header class="topbar">
  <div class="wrap">
    <div class="social"><span><i></i></span><span><i></i></span><span><i></i></span><span><i></i></span></div>
    <div class="contact-top">
      <div><svg width="16" height="16" viewBox="0 0 24 24"><path fill="#fff" d="M6.6 10.8a15 15 0 006.6 6.6l2.2-2.2c.3-.3.7-.4 1-.2 1.1.4 2.3.6 3.6.6.6 0 1 .4 1 1V20c0 .6-.4 1-1 1A17 17 0 013 4c0-.6.4-1 1-1h3.5c.6 0 1 .4 1 1 0 1.3.2 2.5.6 3.6.1.3 0 .7-.2 1z"/></svg>+27 (0) 11 555 0142</div>
      <div><svg width="18" height="14" viewBox="0 0 24 18"><rect x="1" y="1" width="22" height="16" fill="none" stroke="#fff" stroke-width="2"/><path d="M1 1l11 9 11-9" fill="none" stroke="#fff" stroke-width="2"/></svg>info@tarvologistics.co.za</div>
    </div>
  </div>
</header>

<nav class="nav">
  <div class="wrap">
    <div class="brand"><span class="brand-dot"></span>Tarvo</div>
    <div class="menu"><a class="active">Home</a><a>About</a><a>Services</a><a>Projects</a><a>Contact</a></div>
    <div class="search">Search here...<svg width="18" height="18" viewBox="0 0 24 24"><circle cx="10" cy="10" r="7" fill="none" stroke="#e9502a" stroke-width="2.5"/><path d="M15 15l6 6" stroke="#e9502a" stroke-width="2.5"/></svg></div>
  </div>
</nav>

<section class="hero" role="img" aria-label="Two engineers in hard hats and safety vests reviewing plans in front of a bridge">
  <h1><span class="first">Transforming</span>our clients <span class="hl">Vision</span><br>into <span class="hl2">Reality</span></h1>
  <div class="dots"><i></i><i class="on"></i><i></i></div>
</section>

<section class="welcome">
  <div class="wrap">
    <div class="welcome-text">
      <h2>Welcome Tarvo Logistic Plant</h2>
      <p>Tarvo Logistics and Plant Hire (Pty) Ltd is a Black Women owned Construction and Plant Hire company operating mainly from the head office in Kelderton, Gauteng. Tarvo Logistics and Plant Hire (Pty) Ltd was established in 2014, and has worked in various municipal jurisdictions within South Africa.</p>
      <p>Since inception, Tarvo Logistics and Plant Hire (Pty) Ltd has worked on a number of projects. Since inception, Tarvo Logistics and Plant Hire (Pty) Ltd has worked on a number of projects.</p>
      <a class="btn">Read More</a>
    </div>
    <div class="welcome-photo" role="img" aria-label="Road crew laying fresh asphalt with a paving machine"></div>
  </div>
</section>

<section class="band">
  <div class="left">
    <h3>Mission Statement</h3>
    <p>Tarvo Logistics and Plant Hire (Pty) Ltd aims to employ the professional skills of a well accomplished staff in providing efficient and sustainable engineering construction solutions to our clients for the benefit of various stakeholders and community at large. As such, we aim to transform both Public and Private sector visions into realities.</p>
  </div>
  <div class="right">
    <h3>Accreditations and ratings</h3>
    <ul>
      <li><span>BEE <b>Level 2</b> rating</span></li>
      <li><span><b>CIDB grading 7CE</b> and <b>1GB PE</b></span></li>
      <li><span>currently undergoing ISO <b>certification</b> processes which is to be completed during the course of <b>2017</b>.</span></li>
    </ul>
  </div>
</section>

<section class="services">
  <div class="wrap">
    <h2 class="section-title">Our Services</h2>
    <p class="section-sub">Acquiring a track record primarily in the following disciplines,<br>amongst the company's offerings and/ or services</p>
    <div class="cards">
      <div class="card"><div class="card-photo" role="img" aria-label="Road roller compacting a new road surface"></div><h4>Roads &amp; Stormwater</h4><p>Road upgrades and rehabilitation<br>Construction of new Paved roads – Paving...</p><a class="more">READ MORE</a></div>
      <div class="card"><div class="card-photo" role="img" aria-label="Excavator laying large water pipes"></div><h4>Water</h4><p>Grey water reticulations<br>Potable water reticulations</p><a class="more">READ MORE</a></div>
      <div class="card"><div class="card-photo" role="img" aria-label="Paving machine working on a sanitation project"></div><h4>Sanitation</h4><p>Upgrade of Infrastructure – Eradication of<br>bucket systems</p><a class="more">READ MORE</a></div>
    </div>
  </div>
</section>

<section class="achieve">
  <div class="city" role="img" aria-label="Tall glass office towers above a green landscaped base"></div>
  <div class="achieve-body">
    <h3>Tarvo Achieving</h3>
    <p class="lead">We are committed to achieving this through the following :</p>
    <div class="icons">
      <span><svg width="34" height="34" viewBox="0 0 24 24" fill="none" stroke="#fff" stroke-width="1.6"><circle cx="9" cy="8" r="3"/><path d="M3 20c0-4 3-6 6-6s6 2 6 6"/><path d="M16 10h5M16 14h5"/></svg></span>
      <span><svg width="34" height="34" viewBox="0 0 24 24" fill="none" stroke="#fff" stroke-width="1.6"><path d="M3 21h18M6 21V12M11 21V7M16 21v-6"/><path d="M4 8l6-5 5 4 5-3"/></svg></span>
      <span><svg width="34" height="34" viewBox="0 0 24 24" fill="none" stroke="#fff" stroke-width="1.6"><circle cx="12" cy="12" r="9"/><path d="M12 7v5l3 3"/></svg></span>
      <span class="on"><svg width="34" height="34" viewBox="0 0 24 24" fill="none" stroke="#fff" stroke-width="1.6"><circle cx="12" cy="12" r="4"/><path d="M12 2v4M12 18v4M2 12h4M18 12h4M5 5l3 3M16 16l3 3M5 19l3-3M16 8l3-3"/></svg></span>
      <span><svg width="34" height="34" viewBox="0 0 24 24" fill="none" stroke="#fff" stroke-width="1.6"><circle cx="12" cy="12" r="9"/><path d="M3 12h18M12 3c3 3 3 15 0 18M12 3c-3 3-3 15 0 18"/></svg></span>
    </div>
    <h4>Adaptability</h4>
    <p class="desc">Preparing our activities to respond to the demands of the<br>present Southern African and regional Environment.</p>
  </div>
</section>

<section class="projects">
  <div class="wrap">
    <h2 class="section-title">Our Projects</h2>
    <div class="filters"><span class="on">All</span>|<span>Construction</span>|<span>Digging</span>|<span>Renovation</span></div>
    <div class="grid">
      <div class="tile t1 feature" role="img" aria-label="Grader on a construction site"><div class="label"><b>PROJECT 1</b><small>Details</small></div></div>
      <div class="tile t2" role="img" aria-label="Pipeline trench across red earth"></div>
      <div class="tile t3" role="img" aria-label="Workers in safety vests reviewing plans"></div>
      <div class="tile t4" role="img" aria-label="Worker operating a road cutting tool"></div>
      <div class="tile t5" role="img" aria-label="Traffic cones lining a road works lane"></div>
      <div class="tile t6" role="img" aria-label="Excavator digging beside workers"></div>
      <div class="tile t7" role="img" aria-label="Crew at a utility excavation"></div>
      <div class="tile t8" role="img" aria-label="Road roller on fresh asphalt"></div>
    </div>
  </div>
</section>

<section class="ready">
  <h2>Ready To Get started</h2>
  <p>We want to hear from you. Reach out to us with any questions or request for more information.</p>
  <div class="form">
    <div class="field">First Name :</div>
    <div class="field">Last Name :</div>
    <div class="field">Phone Number :</div>
    <div class="field">Email Address :</div>
    <div class="field full">Message / Comments :</div>
    <div class="submit">Submit Now</div>
  </div>
</section>

<footer class="footer">
  <div class="wrap">
    <div>
      <div class="brand"><span class="brand-dot"></span>Tarvo</div>
      <p class="about">We build roads, water and sanitation works that last for the communities we serve.<br><u>READ MORE</u></p>
    </div>
    <div>
      <h5>Useful Links</h5>
      <ul class="links"><li class="on">Home</li><li>About</li><li>Services</li><li>Projects</li><li>Contact</li></ul>
    </div>
    <div>
      <h5>Get In Touch</h5>
      <div class="touch"><svg width="18" height="22" viewBox="0 0 24 30"><path fill="#f39322" d="M12 0a10 10 0 00-10 10c0 8 10 20 10 20s10-12 10-20A10 10 0 0012 0zm0 14a4 4 0 110-8 4 4 0 010 8z"/></svg><div><b>Free State office</b><br>Unit 4, Ridgeway Centre<br>Bloemfontein 9300</div></div>
      <div class="touch"><svg width="18" height="18" viewBox="0 0 24 24"><path fill="#f39322" d="M6.6 10.8a15 15 0 006.6 6.6l2.2-2.2c.3-.3.7-.4 1-.2 1.1.4 2.3.6 3.6.6.6 0 1 .4 1 1V20c0 .6-.4 1-1 1A17 17 0 013 4c0-.6.4-1 1-1h3.5c.6 0 1 .4 1 1 0 1.3.2 2.5.6 3.6.1.3 0 .7-.2 1z"/></svg><div>+27 (0) 11 555 0142</div></div>
      <div class="touch"><svg width="18" height="14" viewBox="0 0 24 18"><rect x="1" y="1" width="22" height="16" fill="#f39322"/><path d="M1 1l11 9 11-9" fill="none" stroke="#fff" stroke-width="2"/></svg><div>info@tarvologistics.co.za</div></div>
    </div>
    <div class="news">
      <h5>Newsletter</h5>
      <p>Would you like to receive exclusive access to articles, white papers and our regular monthly newsletter?</p>
      <div class="sub"><span><svg width="14" height="11" viewBox="0 0 24 18"><rect x="1" y="1" width="22" height="16" fill="#f39322"/></svg>Email</span><i><svg width="20" height="20" viewBox="0 0 24 24"><path fill="#fff" d="M2 12L22 3l-5 19-5-7z"/></svg></i></div>
    </div>
  </div>
</footer>

<div class="copy">Copyright © TARVO LOGISTIC &amp; PLANT HIRE - 2018 . All Right Reserved</div>

</body>
</html>
```